Important Solar Energy Company Needs a Stationery Design

I need a modern, attractive, corporate stationary design (letter head and business card)
Attached Company Logo

Target Market(s)

Upmarket

Industry/Entity Type

Business

Colors
ec1f27
ffffff
757575
cbcbcb
000000

```html
<!DOCTYPE html>
<html lang="en">
<head>
<meta charset="utf-8">
<title>Lumenova Business Card</title>
<link rel="stylesheet" href="https://fonts.googleapis.com/css2?family=Montserrat:wght@400;500;600&display=swap">
<style>
  :root {
    --brand-red: #ec1f27;
    --paper: #ffffff;
    --ink-grey: #757575;
    --backdrop: #e4e4e4;
    --edge: #cbcbcb;
    --ink: #222222;
  }
  * { box-sizing: border-box; margin: 0; padding: 0; }
  html, body { width: 1200px; height: 900px; overflow: hidden; }
  body {
    background: var(--backdrop);
    font-family: "Montserrat", Arial, sans-serif;
    display: flex;
    flex-direction: column;
    align-items: center;
    justify-content: center;
    gap: 60px;
  }
  .card {
    width: 560px;
    height: 320px;
    position: relative;
    overflow: hidden;
    box-shadow: 0 2px 0 var(--edge);
  }
  /* Front */
  .card-front { background: var(--paper); display: flex; flex-direction: column; }
  .front-top {
    flex: 0 0 196px;
    padding: 46px 40px 0 44px;
    display: grid;
    grid-template-columns: 1fr auto;
    grid-template-rows: auto 1fr;
    column-gap: 24px;
  }
  .brand { display: flex; align-items: center; gap: 18px; grid-column: 1 / 3; }
  .brand-dot { width: 52px; height: 52px; border-radius: 50%; background: var(--brand-red); }
  .brand-name {
    font-size: 31px; font-weight: 400; letter-spacing: 3px; color: var(--ink);
  }
  .person { margin-top: 26px; padding-left: 2px; }
  .person-name {
    color: var(--brand-red); font-weight: 600; font-size: 17px; letter-spacing: 1px;
  }
  .person-role {
    color: var(--ink-grey); font-size: 12px; letter-spacing: 1.5px; margin-top: 2px;
  }
  .address {
    margin-top: 26px; color: var(--ink-grey); font-size: 13px; line-height: 1.45; text-align: left;
  }
  .front-band {
    flex: 1;
    background: var(--brand-red);
    color: var(--paper);
    display: flex;
    justify-content: space-between;
    align-items: center;
    padding: 0 40px 0 44px;
    font-size: 13.5px;
    letter-spacing: 0.3px;
  }
  .contact-list { list-style: none; display: flex; flex-direction: column; gap: 7px; }
  .contact-list li { display: flex; align-items: center; gap: 9px; }
  .icon { width: 14px; height: 14px; flex: none; }
  /* Back */
  .card-back {
    background: var(--brand-red);
    display: flex; flex-direction: column; align-items: center; justify-content: center; gap: 22px;
  }
  .back-circle { width: 140px; height: 140px; border-radius: 50%; background: var(--paper); }
  .back-name { color: var(--paper); font-size: 24px; letter-spacing: 4px; font-weight: 400; }
</style>
</head>
<body>
  <article class="card card-front" aria-label="Business card front">
    <div class="front-top">
      <div class="brand">
        <span class="brand-dot"></span>
        <span class="brand-name">LUMENOVA</span>
      </div>
      <div class="person">
        <p class="person-name">MARCO DELVANE</p>
        <p class="person-role">DIRECTOR</p>
      </div>
      <p class="address">228 Harbor Row<br>Dayton, OH 45402</p>
    </div>
    <div class="front-band">
      <ul class="contact-list">
        <li>
          <svg class="icon" viewBox="0 0 14 14"><circle cx="7" cy="7" r="6.3" fill="none" stroke="#fff" stroke-width="1.2"/><rect x="5" y="3.5" width="4" height="7" rx="0.8" fill="none" stroke="#fff" stroke-width="1"/></svg>
          05550 481 260
        </li>
        <li>
          <svg class="icon" viewBox="0 0 14 14"><circle cx="7" cy="7" r="6.3" fill="none" stroke="#fff" stroke-width="1.2"/><path d="M4 8.5 Q7 3 10 8.5 Z" fill="#fff"/></svg>
          05550 481 261
        </li>
      </ul>
      <ul class="contact-list">
        <li>
          <svg class="icon" viewBox="0 0 14 14"><circle cx="7" cy="7" r="6.3" fill="none" stroke="#fff" stroke-width="1.2"/><rect x="3.8" y="4.8" width="6.4" height="4.4" fill="none" stroke="#fff" stroke-width="1"/><path d="M3.8 4.8 L7 7.4 L10.2 4.8" fill="none" stroke="#fff" stroke-width="1"/></svg>
          mdelvane@lumenova.com
        </li>
        <li>
          <svg class="icon" viewBox="0 0 14 14"><circle cx="7" cy="7" r="6.3" fill="none" stroke="#fff" stroke-width="1.2"/><circle cx="7" cy="7" r="3.4" fill="none" stroke="#fff" stroke-width="0.9"/><path d="M3.6 7 H10.4 M7 3.6 V10.4" stroke="#fff" stroke-width="0.9"/></svg>
          www.lumenova.com
        </li>
      </ul>
    </div>
  </article>

  <article class="card card-back" aria-label="Business card back">
    <span class="back-circle"></span>
    <span class="back-name">LUMENOVA</span>
  </article>
</body>
</html>
```